Create a Graphic About YOURSELF and PixelHarbor

PixelHarbor would like you (designers) to create an awesome graphic to promote YOURSELF and your profile on PixelHarbor!

Your graphic should communicate your name, your services and should mention PixelHarbor.

The design should be perfect for sharing on Chatterly. Here's an example of what we'd like http://blog.pixelharbor-example.ca/article/333/pixelharbor-launches-3000-hire-me-social-design-contest

Once you submitted your design, we'd love you to share the design ('advertisement') and promote yourself and PixelHarbor to your friends and potential customers. So make your submissions great and get your friends to vote for your design by 'Liking' it on Chatterly!

Prizes:
$1500 - "PixelHarbor Community" prize awarded to the designer with the most Chatterly 'Likes'
5 x $50 for the next 5 'most liked' designs on Chatterly

$1000 - "Hire Me" prize awarded to the designer who receives the most client invites
5 x $50 for the next 5 'most invited' designers

In summary, this is a great opportunity for you to increase your exposure to PixelHarbor customers and win cash prizes. Show off your design skills and get hired by PixelHarbor customers from around the world!

Target Market(s)

Fans, friends and customers of YOU

Industry/Entity Type

Cash

Requirements
Must have
• 1) Include your PixelHarbor user name on the graphic so customers can find you in the PixelHarbor Designer Directory
2) Include the tagline "Hire Me on PixelHarbor.com!" in your graphic design.
3) Share your design's URL on our Chatterly wall at http://chatterly-example.com/pixelharbor and get your friends to 'like' your design.
Nice to have
• 1) Include a tagline that expresses your design approach/philosophy
2) Artwork dimensions: 403 x 403 px
3) You can submit more than 1 design!
Should not have
• You must own the copyright of any images you use including stock imagery.

```html
<!DOCTYPE html>
<html lang="en">
<head>
<meta charset="utf-8">
<title>VEKO Logo Design – Hire Me</title>
<link href="https://fonts.googleapis.com/css2?family=Oswald:wght@500;600;700&display=swap" rel="stylesheet">
<style>
  :root {
    --paper: #ffffff;
    --crimson: #d41a50;
    --charcoal: #333333;
    --ocean: #1b6592;
    --bar: #3a3a3a;
    --slate: #4a4a4a;
    --white: #ffffff;
  }
  * { box-sizing: border-box; margin: 0; padding: 0; }
  html, body { width: 1200px; height: 900px; overflow: hidden; background: var(--paper); }
  body { font-family: "Oswald", "Arial Narrow", sans-serif; position: relative; }

  .brand-block { position: absolute; left: 148px; top: 112px; width: 300px; }
  .brand-name {
    color: var(--crimson); font-weight: 700; font-size: 158px; line-height: 1;
    letter-spacing: -1px; text-align: center; height: 150px; white-space: nowrap;
  }
  .brand-service {
    color: var(--charcoal); font-weight: 600; font-size: 70px; line-height: 1;
    letter-spacing: -1px; text-align: center; margin-top: 6px; white-space: nowrap;
  }

  .hire-panel {
    margin-top: 24px; height: 106px; background: var(--ocean);
    display: flex; align-items: center; justify-content: center;
    color: var(--white); font-weight: 600; font-size: 54px; letter-spacing: 0;
  }
  .panel-notch { display: block; width: 300px; height: 30px; }

  .profile-panel {
    height: 110px; background: var(--ocean); margin-top: -4px;
    display: flex; align-items: center; justify-content: center; gap: 14px;
    color: var(--white); font-weight: 600; font-size: 40px;
  }
  .profile-panel .dot { width: 22px; height: 22px; border-radius: 50%; background: var(--white); }

  .side-tag {
    position: absolute; left: 1040px; top: 24px; width: 118px; height: 36px;
    background: var(--slate); color: var(--white); font-weight: 600; font-size: 24px;
    display: flex; align-items: center; justify-content: center;
  }
  .side-stripes { position: absolute; left: 1040px; top: 60px; width: 140px; height: 710px; }

  .tagline-bar {
    position: absolute; left: 0; top: 796px; width: 1200px; height: 68px;
    background: var(--bar); color: var(--white);
    display: flex; align-items: center; justify-content: center;
  }
  .tagline { font-weight: 600; font-size: 29px; }
</style>
</head>
<body>
  <main class="brand-block">
    <h1 class="brand-name">VEKO</h1>
    <p class="brand-service">LOGODESIGN</p>

    <div class="hire-panel">HIRE ME</div>
    <svg class="panel-notch" viewBox="0 0 300 30" aria-hidden="true">
      <polygon points="124,6 176,6 150,26" fill="#1b6592"/>
    </svg>
    <div class="profile-panel">
      <span class="dot"></span>
      <span>PixelHarbor</span>
    </div>
  </main>

  <div class="side-tag">VEKO</div>
  <svg class="side-stripes" viewBox="0 0 140 710" role="img" aria-label="Vertical textured stripes in blue, crimson and charcoal">
    <defs>
      <linearGradient id="stripe-blue" x1="0" y1="0" x2="0" y2="1">
        <stop offset="0" stop-color="#8fb0c6"/><stop offset="1" stop-color="#1b6592"/>
      </linearGradient>
      <linearGradient id="stripe-red" x1="0" y1="0" x2="0" y2="1">
        <stop offset="0" stop-color="#e9a0b4"/><stop offset="1" stop-color="#d41a50"/>
      </linearGradient>
      <linearGradient id="stripe-dark" x1="0" y1="0" x2="0" y2="1">
        <stop offset="0" stop-color="#a6a6a6"/><stop offset="1" stop-color="#3a3a3a"/>
      </linearGradient>
    </defs>
    <polygon points="46,0 72,0 59,12" fill="#4a4a4a"/>
    <rect x="2" y="20" width="16" height="610" fill="url(#stripe-blue)"/>
    <rect x="32" y="20" width="14" height="470" fill="url(#stripe-red)"/>
    <rect x="58" y="20" width="16" height="564" fill="url(#stripe-dark)"/>
    <rect x="88" y="20" width="14" height="470" fill="url(#stripe-red)"/>
    <rect x="116" y="20" width="16" height="686" fill="url(#stripe-blue)"/>
  </svg>

  <footer class="tagline-bar">
    <p class="tagline">Hire Me on PixelHarbor.com!</p>
  </footer>
</body>
</html>
```